International Manufacturing Business Needs A Heavy Hitting Wordpress Design!

We need wordpress template designs for a new website for our UK based International company Halvenmoor Fabrication Ltd. We manufacture and supply steel security doors and window units. We would like designs that feature the black and yellow industrial "stripes" that can be seen at our current site www.pelbrogates.com. The final design should communicate strength, power and weight to represent the quality of the products and the security that they provide.

It feels like we need 3 different types of page to be able to be created as per the current website at www.pelbrostrongdoors.com.

Homepage
Products/Accessories
Leadtimes/Downloads/Contact

It may be that 3 different page types can be created with one template. I'm totally open to this.

I don't like the way that the site currently handles product images, nobody wants to click on even thumbnail to see the product. http://pelbrostrongdoors.com/products/personnel-doors/

Totally open to suggestions on layout to enable the feeling outlined in the brief above.

Please ask if anything is not clear or you need answers to drill down on specifics.

Target Market(s)

Businesses that buy steel doors

Font styles to use
Sans Serif
Other font styles liked:
• Copperplate Gothic Bold - For Company Name but we are open to suggestions

Colors

Designer to choose colors to be used in the design.

Requirements
Must have
• Professional looking, clean design
• Conveys strength, power and weight to represent the quality of the products, the characteristics of steel and the security that they provide.
• Incorporates black and yellow stripes of our branding
• Ability to create pages with content as seen at www.pelbrostrongdoors.com
• A better way of showing the product images
Nice to have
• If possible. a design that gives off the feeling that not only do we supply the products we also make them in house too. I don't know what this looks like but a way of differentiating between a supply only business and one that manufacturers the product too.
Should not have
• We don't like the current thumbnail method of showing the product images

```html
<!DOCTYPE html>
<html lang="en">
<head>
<meta charset="utf-8">
<title>Halvenmoor Fabrication Ltd</title>
<link rel="stylesheet" href="https://fonts.googleapis.com/css2?family=Arimo:wght@400;700&family=Questrial&display=swap">
<style>
:root{
  --yellow:#fff200;
  --teal:#5e9e9e;
  --ink:#222;
  --text:#333;
  --light:#f2f2f2;
  --bar:rgba(38,42,48,.88);
  --footer:#1f2a33;
  --base:#121417;
  --badge:#d9d9d9;
  --social:#5b7c9c;
}
*{box-sizing:border-box;margin:0;padding:0}
html,body{width:1200px;height:2616px;overflow:hidden}
body{position:relative;background:#fff;font-family:"Arimo",Arial,sans-serif;color:var(--text)}
.abs{position:absolute}

/* hero */
.hero-photo{left:0;top:0;width:1200px;height:593px;
  background:linear-gradient(100deg,#4a3d2e 0%,#bfb3a0 22%,#e9e4da 45%,#d8cbb6 62%,#efeeea 80%,#c9c4bb 100%)}
.topbar{left:0;top:0;width:1200px;height:70px;background:var(--bar)}
.brand{left:96px;top:14px;display:flex;align-items:center;gap:10px;color:#fff;font-family:"Questrial",Arial,sans-serif}
.brand .mark{width:20px;height:38px;background:var(--teal)}
.brand .name{font-size:19px;line-height:18px;letter-spacing:1px}
.brand .name small{display:block;font-size:11px;letter-spacing:1.5px}
.nav{font-size:11px;color:#fff;top:29px}
.nav-products{left:602px;top:0;width:110px;height:223px;background:var(--yellow)}
.nav-products span{position:absolute;top:29px;left:0;width:110px;text-align:center;font-size:11px;color:#222}
.dropdown{left:712px;top:70px;width:129px;height:153px;background:var(--yellow);padding:10px 0 0 17px;font-size:9px;line-height:19px;color:#222}
.dropdown-cats{left:620px;top:80px;font-size:9px;line-height:19px;color:#222}
.btn-download{left:841px;top:23px;width:132px;height:24px;background:var(--teal);color:#fff;font-size:11px;text-align:center;line-height:24px}
.socials{display:flex;gap:6px}
.socials i{display:block;width:20px;height:20px;background:var(--social);border-radius:3px}
.hero-caption{left:776px;top:436px;width:424px;height:110px;background:rgba(45,50,56,.8);color:#fff;text-align:right;padding:20px 22px 0 0;font-family:"Questrial",Arial,sans-serif}
.hero-caption .kicker{font-size:21px;letter-spacing:.5px}
.hero-caption .cta{font-size:38px;line-height:44px}

/* order + contact */
.order-band{left:0;top:610px;width:1200px;height:569px;background:var(--light)}
.section-title{font-family:"Questrial",Arial,sans-serif;font-size:31px;color:var(--ink)}
.intro{left:256px;top:767px;width:340px;font-size:13px;line-height:19px}
.field{left:256px;width:340px;background:#fff;border-radius:2px;font-size:11px;color:#444;padding:8px 18px}
.btn-order{left:256px;top:1052px;width:161px;height:25px;background:var(--teal);color:#fff;font-size:12px;text-align:center;line-height:25px}
.contact-row{left:718px;display:flex;gap:13px;font-size:13px;line-height:20px}
.contact-row svg{flex:none;margin-top:2px}

/* door feature */
.door-photo{left:0;top:1179px;width:1200px;height:462px;
  background:linear-gradient(90deg,#1d1f22 0%,#3b3a37 18%,#2c2a28 38%,#4a4a4a 62%,#2a2a2a 82%,#141414 100%)}
.door-title{left:0;top:1350px;width:1200px;text-align:center;font-family:"Questrial",Arial,sans-serif;font-size:54px;color:var(--yellow)}
.door-copy{left:355px;top:1424px;width:490px;text-align:center;color:#fff;font-size:12px;line-height:20px}

/* showcase */
.house-photo{left:239px;top:1754px;width:722px;height:414px;
  background:linear-gradient(180deg,#3f6fae 0%,#7fa3d0 45%,#3d3a33 70%,#5a3c2c 100%)}
.showcase-copy{left:200px;top:2218px;width:800px;text-align:center;font-size:17px;line-height:25.5px;color:#333}

/* footer */
.footer{left:0;top:2438px;width:1200px;height:129px;background:var(--footer)}
.footer-address{left:380px;top:2476px;width:286px;text-align:center;color:#fff;font-size:16px;line-height:25px}
.badges{left:733px;top:2480px;display:flex;gap:6px}
.badges i{display:block;height:49px;background:var(--badge)}
.base{left:0;top:2567px;width:1200px;height:49px;background:var(--base)}
.copyright{left:166px;top:2587px;color:#fff;font-size:10px}
</style>
</head>
<body>

<div class="abs hero-photo" role="img" aria-label="Bright modern open-plan living and kitchen interior with a patterned screen"></div>
<div class="abs topbar"></div>
<div class="abs brand"><span class="mark"></span><span class="name">HALVENMOOR<small>FABRICATION LTD.</small></span></div>
<div class="abs nav-products"><span>PRODUCTS</span></div>
<div class="abs nav" style="left:537px">HOME</div>
<div class="abs nav" style="left:731px">CONTACT</div>
<div class="abs dropdown-cats">Products &nbsp;&nbsp;&gt;<br>Accessories &nbsp;&gt;</div>
<div class="abs dropdown">• Personnel Doors<br>• Fire Exit Doors<br>• Blank Doors<br>• Acoustic Doors<br>• Anti-vandal shutters<br>&nbsp;&nbsp;and glazing uni<br>• Technical Videos</div>
<div class="abs btn-download">DOWNLOAD</div>
<div class="abs socials" style="left:1003px;top:25px"><i></i><i></i><i></i><i></i></div>
<div class="abs hero-caption">
  <div class="kicker">HALVENMOOR FABRICATION,</div>
  <div class="cta">Get It Now!!!</div>
</div>

<svg class="abs" style="left:0;top:593px" width="1200" height="17" viewBox="0 0 1200 17">
  <rect width="1200" height="17" fill="#111"/>
  <g fill="#fff200">
    <polygon points="136,0 272,0 266,17 130,17"/>
    <polygon points="408,0 542,0 536,17 402,17"/>
    <polygon points="678,0 804,0 798,17 672,17"/>
    <polygon points="944,0 1074,0 1068,17 938,17"/>
  </g>
</svg>

<div class="abs order-band"></div>
<h2 class="abs section-title" style="left:256px;top:700px">Buy Our Door Now!</h2>
<p class="abs intro">Lorem Ipsum is simply dummy text of the printing and typesetting industry. Lorem Ipsum has been the industry's standard dummy text ever since the 1500s.</p>
<div class="abs field" style="top:858px;height:30px">Name</div>
<div class="abs field" style="top:902px;height:29px">Email</div>
<div class="abs field" style="top:945px;height:93px">How can we help?</div>
<div class="abs btn-order">ORDER NOW!</div>

<h2 class="abs section-title" style="left:718px;top:700px">Contact Us</h2>
<div class="abs contact-row" style="top:760px">
  <svg width="18" height="20" viewBox="0 0 18 20"><path d="M9 0a7 7 0 0 1 7 7c0 5-7 13-7 13S2 12 2 7a7 7 0 0 1 7-7z" fill="#5e9e9e"/><circle cx="9" cy="7" r="2.6" fill="#f2f2f2"/></svg>
  <span>Halvenmoor Fabrication Ltd.<br>Ashby Forge, Millrace Lane,<br>Thornwick, Hull UK, HU14 7QD.</span>
</div>
<div class="abs contact-row" style="top:841px">
  <svg width="18" height="18" viewBox="0 0 18 18"><circle cx="9" cy="9" r="9" fill="#5e9e9e"/><path d="M5.5 4.5l2 .2.8 2.2-1.2 1a6 6 0 0 0 3 3l1-1.2 2.2.8.2 2c-4.5.6-8.6-3.5-8-8z" fill="#f2f2f2"/></svg>
  <span>+44 (0) 1632 960418<br>+44 (0) 1632 960427</span>
</div>
<div class="abs contact-row" style="top:900px">
  <svg width="18" height="18" viewBox="0 0 18 18"><circle cx="9" cy="9" r="9" fill="#5e9e9e"/><rect x="4.5" y="6" width="9" height="6.5" fill="#f2f2f2"/><path d="M4.5 6l4.5 3.6L13.5 6" fill="none" stroke="#5e9e9e" stroke-width="1"/></svg>
  <span>info@halvenfab-doors.co.uk</span>
</div>

<div class="abs door-photo" role="img" aria-label="Dark interior with tall timber and frosted glass doors, armchair and vases"></div>
<h2 class="abs door-title">Loren Ipsum Door</h2>
<p class="abs door-copy">Lorem Ipsum is simply dummy text of the printing and typesetting industry. Lorem<br>Ipsum has been the industry's standard dummy text ever since the 1500s.</p>

<div class="abs house-photo" role="img" aria-label="Modern two-storey house at dusk with lit windows and palm trees"></div>
<p class="abs showcase-copy">Halvenmoor steel security doors are the ideal solution for a wide range of applications<br>in which security, quality and cost are all essential requirements.<br>Halvenmoor steel security doors are the ideal solution for a wide range of applications<br>in which security, quality and cost are all essential requirements.</p>

<footer>
  <div class="abs footer"></div>
  <div class="abs brand" style="left:162px;top:2482px"><span class="mark"></span><span class="name">HALVENMOOR<small>FABRICATION LTD.</small></span></div>
  <div class="abs footer-address">Ashby Forge, Thornwick,<br>Hull, HU14 7QD</div>
  <div class="abs badges" aria-label="Accreditation badges"><i style="width:79px"></i><i style="width:78px"></i><i style="width:115px;background:#b8643a"></i></div>
  <div class="abs base"></div>
  <div class="abs copyright">© Copyright 2018 &nbsp;|&nbsp; HALVENMOOR FABRICATION</div>
  <div class="abs socials" style="left:1003px;top:2581px"><i></i><i></i><i></i><i></i></div>
</footer>

</body>
</html>
```